Brill Insurance Agency - Business Cards

Hello, I am needing new trendy business cards for our Insurance Agency now that I have a new Logo. I have attached our new logo with several color options along with a business card design that I like. I am leaning towards burgundy and blue colors. I have attached our current business card. I have also attached a headshot of our company president, Martin Vale, that you can use if you wish. Thank you so much in advance for all the wonderful designs!!!!

Target Market(s)

We want to look very professional to potential customers and we also want to look very professional so insurance companies will want to contract with us to sell their product.

Industry/Entity Type

Insurance

Contact Information for Business Card

Martin Vale
mvale@brillagency.com
Business: 555-213-4087
Fax: 555-213-7751
Cell: 555-390-2618
Toll Free: 888-555-0194
42 W Elm Rd Elmdale, KS 66999
www.brillagency.net

Font styles to use
Serif
Sans Serif

Colors
0355a3
3277b5
f04a50
ec1f27

Requirements
Nice to have
• I love creativity. The more creative and balanced a business card design the more I will like it. I would like the card to be printed horizontally instead of vertically.
Should not have
• My project should not have the Allied Coverage Network logo. It is no longer used in the industry.

```html
<!DOCTYPE html>
<html lang="en">
<head>
<meta charset="utf-8">
<title>Brill Insurance Agency – Business Cards</title>
<link rel="stylesheet" href="https://fonts.googleapis.com/css2?family=Source+Sans+3:wght@400;600;700&display=swap">
<style>
  :root {
    --page-bg: #ececec;
    --card-white: #ffffff;
    --navy: #1f2a5e;
    --slate: #4a4a4a;
    --text-light: #ffffff;
  }
  * { box-sizing: border-box; margin: 0; padding: 0; }
  html, body {
    width: 1200px;
    height: 900px;
    overflow: hidden;
    background: var(--page-bg);
    font-family: "Source Sans 3", "Helvetica Neue", Arial, sans-serif;
  }
  .canvas {
    position: relative;
    width: 1200px;
    height: 900px;
  }
  .card {
    position: absolute;
    left: 320px;
    width: 560px;
    height: 320px;
    background: var(--card-white);
    box-shadow: 0 2px 6px rgba(0,0,0,0.18);
    overflow: hidden;
  }
  .card--front { top: 105px; }
  .card--back { top: 475px; }

  .brand {
    position: absolute;
    left: 50%;
    transform: translate(-50%, -50%);
    display: flex;
    align-items: center;
    gap: 16px;
    white-space: nowrap;
  }
  .card--front .brand { top: 160px; }
  .card--back .brand { top: 86px; }
  .brand__mark {
    width: 70px;
    height: 70px;
    border-radius: 50%;
    border: 7px solid var(--slate);
  }
  .card--back .brand__mark { width: 60px; height: 60px; border-width: 6px; }
  .brand__name {
    color: var(--navy);
    font-weight: 700;
    font-size: 27px;
    line-height: 1.05;
    letter-spacing: 0.3px;
    text-transform: uppercase;
  }
  .card--back .brand__name { font-size: 23px; }

  .contact-band {
    position: absolute;
    left: 0;
    right: 0;
    top: 160px;
    bottom: 0;
    background: var(--navy);
  }
  .name-tab {
    position: absolute;
    left: 139px;
    top: 147px;
    width: 284px;
    height: 40px;
    background: var(--slate);
    color: var(--text-light);
    font-weight: 700;
    font-size: 23px;
    line-height: 1;
    display: flex;
    align-items: center;
    justify-content: center;
    padding-top: 6px;
  }
  .contact-list {
    position: absolute;
    top: 199px;
    list-style: none;
    color: var(--text-light);
    font-size: 17px;
    line-height: 26.5px;
    white-space: nowrap;
  }
  .contact-list--phones { left: 35px; }
  .contact-list--web { left: 342px; }
  .contact-list .address { line-height: 18px; padding-top: 5px; }
</style>
</head>
<body>
<main class="canvas">
  <section class="card card--front" aria-label="Business card front">
    <div class="brand">
      <span class="brand__mark" aria-hidden="true"></span>
      <span class="brand__name">Brill Insurance<br>Agency Inc</span>
    </div>
  </section>

  <section class="card card--back" aria-label="Business card back">
    <div class="brand">
      <span class="brand__mark" aria-hidden="true"></span>
      <span class="brand__name">Brill Insurance<br>Agency Inc</span>
    </div>
    <div class="contact-band"></div>
    <div class="name-tab">Martin Vale</div>
    <ul class="contact-list contact-list--phones">
      <li>Business: 555-213-4087</li>
      <li>Fax: 555-213-7751</li>
      <li>Cell: 555-390-2618</li>
      <li>Toll Free: 888-555-0194</li>
    </ul>
    <ul class="contact-list contact-list--web">
      <li>mvale@brillagency.com</li>
      <li>www.brillagency.net</li>
      <li class="address">42 W Elm Rd Elmdale,<br>KS 66999</li>
    </ul>
  </section>
</main>
</body>
</html>
```